Bold & Sexy Pagekiln Affiliate website. URL www.MabelsTrinketNook.com

I have hired a Gigstall to setup an Affiliate Website with Brontex. We need Bold & Sexy Pagekiln website. Target market men. URL www.MabelsTrinketNook.com. More bold & sexy than our book cover. See attached. Use a pagekiln template that my Gigstall can use. I need your experience in design and proper choice of pagekiln template because I do not have the tech skills. I do not want it to look like a traditional "page of things to buy". I would like an image and a short story to go with almost every item for sale. Maybe show me a quick template before you move forward. Any experience and input would be appreciated. Thank you See attached as to a look I do NOT want.
Color: I like a fiery note red, orange, yellow.
Please make me aware of additional services you provide and There may be a delay in my response to you. I need to work my day job to pay for this.
Updates

To clarify the URL for this new website is www.MabelsTrinketNook.com

Target Market(s)

Target market men. URL www.MabelsTrinketNook.com

Number of Pages Required

1 page

Colors
FFC000
F8CF3A
FAE287
FDF2CF
FEFAEE
EE7325
F08F49
F5BC92
FAE3D3
FDF4ED
EB3D1F
EC4F4E
F09395
F8D3D4
FCEDEE

Requirements
Should not have
• Men excercising

```html
<!DOCTYPE html>
<html lang="en">
<head>
<meta charset="utf-8">
<title>Mabels Trinket Nook</title>
<link rel="stylesheet" href="https://fonts.googleapis.com/css2?family=DM+Serif+Display&family=Montserrat:wght@400;500;600;700;800&display=swap">
<style>
:root{
  --ink:#111111;
  --muted:#8a8a8a;
  --white:#ffffff;
  --blush:#e9d0d1;
  --rose:#d9607f;
  --fire:#eb3d1f;
  --fire-soft:#ec4f4e;
  --orange:#ee7325;
  --orange-soft:#f08f49;
  --peach:#f5bc92;
  --yellow:#ffc000;
  --yellow-soft:#fae287;
  --charcoal:#2e2e30;
  --grey:#f0f0f0;
  --footer:#f2f2f2;
  --serif:'DM Serif Display', Georgia, serif;
  --sans:'Montserrat', Arial, sans-serif;
}
*{box-sizing:border-box;margin:0;padding:0}
html,body{width:1200px;height:4202px;overflow:hidden}
body{position:relative;background:var(--white);font-family:var(--sans);color:var(--ink)}
.abs{position:absolute}
.btn{position:absolute;display:flex;align-items:center;justify-content:center;font:700 10px var(--sans);letter-spacing:.5px;text-transform:uppercase}
.btn-dark{background:var(--ink);color:var(--white)}
.btn-outline{border:2px solid var(--ink);color:var(--ink);background:transparent}
.btn-light{border:1.5px solid var(--white);color:var(--white)}
.photo{position:absolute}
.product-shot{position:absolute;border-radius:18px;background:linear-gradient(160deg,#4a4a4e 0%,var(--charcoal) 55%,#1c1c1e 100%);box-shadow:0 18px 30px rgba(0,0,0,.18)}

/* hero */
.hero{position:absolute;left:0;top:0;width:1200px;height:637px;background:linear-gradient(90deg,#ecd6d6 0%,#e6cacb 60%,#dcb9bb 100%)}
.nav{position:absolute;top:27px;left:32px;display:flex;gap:18px;font:700 11px var(--sans)}
.nav-right{position:absolute;top:24px;right:24px;display:flex;align-items:center;gap:18px;font:700 11px var(--sans)}
.nav-right .search{width:34px;height:34px;display:flex;align-items:center;justify-content:center;background:rgba(255,255,255,.25)}
.nav-right .login{font-weight:500;margin-left:24px}
.brand{position:absolute;display:flex;align-items:center;gap:8px;font:20px var(--serif);color:var(--rose);white-space:nowrap}
.brand .dot{width:14px;height:14px;border-radius:50%;background:var(--rose)}
.hero-ring{position:absolute;left:367px;top:147px;width:470px;height:470px;border-radius:50%;border:1px solid rgba(255,255,255,.55);background:rgba(255,255,255,.12)}
.hero-title{position:absolute;left:196px;top:200px;font:40px/45px var(--serif)}
.hero-sub{position:absolute;left:199px;top:304px;font:500 11px/15px var(--sans)}
.hero-photo{position:absolute;left:470px;top:140px;width:600px;height:480px;border-radius:240px 240px 40px 40px;background:linear-gradient(150deg,#d8a9a3 0%,#cf5b52 38%,#b8443c 48%,#3a3336 70%,#c8a4a2 100%);opacity:.9}

/* promo row */
.kicker{position:absolute;left:66px;top:728px;font:800 21px var(--sans)}
.big{position:absolute;left:60px;top:760px;font:62px/63px var(--serif);text-transform:uppercase}
.card-red{position:absolute;left:805px;top:648px;width:395px;height:479px;background:linear-gradient(135deg,#f04a2a 0%,#e94040 55%,#ec4f4e 100%);color:var(--white)}
.card-red h3{position:absolute;left:47px;top:322px;font:600 15px var(--sans)}
.card-red p{position:absolute;left:46px;top:348px;width:320px;font:400 9.5px/15px var(--sans)}
.card-red .price{position:absolute;left:49px;top:430px;font:600 11px var(--sans)}

/* orange band */
.band{position:absolute;left:0;top:1140px;width:1200px;height:485px;background:linear-gradient(100deg,#f5bc92 0%,#f08f49 45%,#ee7325 60%,#f5bc92 100%)}
.band h2{position:absolute;left:59px;top:122px;font:37px/37px var(--serif)}
.band p{position:absolute;left:60px;top:256px;width:440px;font:500 11px/15px var(--sans)}

/* product split */
.prod-name{position:absolute;font:700 16px var(--sans)}
.prod-text{position:absolute;font:400 10px/17px var(--sans);color:var(--muted)}
.studio{position:absolute;background:linear-gradient(180deg,#f5f5f5 0%,#ececec 100%)}

/* testimonials */
.testi{position:absolute;left:0;top:2250px;width:1200px;height:503px;background:linear-gradient(120deg,#c2381c 0%,#9a2c17 30%,#7a2414 45%,#b8351b 65%,#e0471f 100%);color:var(--white);text-align:center}
.testi .eyebrow{position:absolute;left:0;right:0;top:104px;font:700 10px var(--sans)}
.testi h2{position:absolute;left:0;right:0;top:126px;font:39px var(--serif)}
.testi p{position:absolute;left:300px;right:300px;top:204px;font:400 11.5px/19px var(--sans)}
.testi .client{position:absolute;left:0;right:0;top:285px;font:italic 400 11px var(--sans)}

/* care */
.care-eyebrow{position:absolute;left:193px;top:2918px;font:700 8px var(--sans)}
.care-title{position:absolute;left:191px;top:2944px;font:500 22px/23px var(--sans);text-transform:uppercase}
.care-text{position:absolute;left:193px;top:3000px;width:290px;font:400 10px/17px var(--sans);color:var(--muted)}

/* trending */
.trend-eyebrow{position:absolute;left:0;right:0;top:3298px;text-align:center;font:700 8px var(--sans)}
.trend-title{position:absolute;left:0;right:0;top:3312px;text-align:center;font:44px var(--serif)}
.tile{position:absolute;top:3380px;width:393px;height:392px;background:linear-gradient(180deg,#f4f4f4 0%,#e9e9e9 100%)}
.tile .product-shot{left:70px;top:70px;width:253px;height:252px}
.tile-meta{position:absolute;top:3790px}
.stars{display:flex;gap:2px}
.stars span{width:7px;height:7px;border:1px solid #bbb;border-radius:50%}
.tile-meta h4{font:16px var(--serif);text-transform:uppercase;margin-top:5px}
.tile-meta .p{font:600 8px var(--sans);color:#555;margin-top:4px}

/* footer */
.footer{position:absolute;left:0;top:3891px;width:1200px;height:311px;background:var(--footer)}
.fcol{position:absolute;top:66px;font:400 10px/19px var(--sans);color:#333}
.fcol h5{font:700 8px var(--sans);margin-bottom:40px}
.fcol .addr{color:var(--muted)}
.copy{position:absolute;left:196px;top:291px;font:400 9px var(--sans)}
.social{position:absolute;top:287px;display:flex;gap:12px;left:925px}
.social span{width:18px;height:18px;background:var(--white);border-radius:2px}
</style>
</head>
<body>

<!-- hero -->
<section class="hero">
  <nav class="nav"><span>HOME</span><span>PRODUCTS</span><span>ABOUT</span><span>CONTACT</span></nav>
  <div class="brand" style="left:0;right:0;top:68px;justify-content:center"><span class="dot"></span>Mabels Trinket Nook</div>
  <div class="nav-right">
    <span class="search"><svg width="12" height="12" viewBox="0 0 12 12" aria-hidden="true"><circle cx="5" cy="5" r="3.6" fill="none" stroke="#111" stroke-width="1.4"/><line x1="7.6" y1="7.6" x2="11" y2="11" stroke="#111" stroke-width="1.4"/></svg></span>
    <span style="margin-left:24px">$0.00</span>
    <svg width="20" height="18" viewBox="0 0 20 18" aria-hidden="true"><path d="M1 3h3l2 9h10l2-7H5" fill="none" stroke="#111" stroke-width="1.6"/><circle cx="8" cy="15" r="1.5" fill="#111"/><circle cx="15" cy="15" r="1.5" fill="#111"/><circle cx="17" cy="3" r="4" fill="#111"/></svg>
    <span class="login">LOG IN</span>
  </div>
  <div class="hero-ring"></div>
  <div class="hero-photo" role="img" aria-label="Model in a red swimsuit reclining on the adjustable weight bench"></div>
  <h1 class="hero-title">Vantro Adjustable<br>Weight Bench</h1>
  <p class="hero-sub">Foldable Workout Bench Press for Full Body<br>Strength Training, Incline Decline Bench<br>with Fast Folding - 2023 Version</p>
  <div class="btn btn-dark" style="left:193px;top:385px;width:91px;height:27px">Shop now</div>
</section>

<!-- promo row -->
<p class="kicker">HELPING GUYS GET</p>
<h2 class="big">Hot<br>Sweaty<br>&amp; Hard</h2>
<div class="btn btn-outline" style="left:60px;top:968px;width:95px;height:27px">Read more</div>
<div class="photo" role="img" aria-label="Glamour photo of a woman in a red baseball cap" style="left:400px;top:648px;width:394px;height:479px;background:linear-gradient(175deg,#8c4a3a 0%,#d0342a 14%,#c98d70 30%,#d9a88a 55%,#b98a72 80%,#e2d2c8 100%)"></div>
<div class="card-red">
  <div class="product-shot" role="img" aria-label="Adjustable dumbbell and barbell set" style="left:95px;top:30px;width:205px;height:240px"></div>
  <h3>PRODUCT NAME 6</h3>
  <p>Lorem ipsum dolor sit amet, consectetur adipiscing elit, sed do eiusmod tempor incididunt ut labore et dolore magna adipiscing elit, sed do eiusmod tempor incididunt ut labore et dolore magna</p>
  <span class="price">$ 140.00</span>
  <div class="btn btn-light" style="left:110px;top:425px;width:96px;height:25px;font-size:9px">Add to cart</div>
</div>

<!-- orange band -->
<section class="band">
  <h2>Corlane Adjustable<br>Folding Sit Up Bench<br>Workout</h2>
  <p>Trangular Support Design which highly support the balance and stability. Thousands of weight test to make sure the safety for workout everytime. The situp bench equip with 0.6" thickened steel pipe and 330LBS maximum user weight guarantee which is stable and durable.</p>
  <div class="btn btn-dark" style="left:59px;top:344px;width:91px;height:27px">Shop now</div>
  <div class="product-shot" role="img" aria-label="Folding sit up bench" style="left:600px;top:40px;width:470px;height:390px"></div>
</section>

<!-- product split -->
<div class="photo" role="img" aria-label="Model holding dumbbells against a black backdrop" style="left:0;top:1638px;width:599px;height:612px;background:linear-gradient(90deg,#000 0%,#120c09 22%,#4a3024 45%,#6a4634 52%,#3a261c 62%,#0e0907 80%,#000 100%)"></div>
<div class="studio" style="left:723px;top:1757px;width:353px;height:219px">
  <div class="product-shot" role="img" aria-label="Recumbent exercise bike" style="left:95px;top:30px;width:163px;height:160px;border-radius:14px"></div>
</div>
<h3 class="prod-name" style="left:720px;top:1996px">PRODUCT NAME 9</h3>
<p class="prod-text" style="left:720px;top:2025px;width:270px">Lorem ipsum dolor sit amet, consectetur adipiscing elit. Ut elit tellus, luctus nec ullamcorper mattis, pulvinar dapibus leo.</p>
<span class="abs" style="left:727px;top:2118px;font:400 10px var(--sans);color:var(--muted)">$135.00</span>
<div class="btn btn-outline" style="left:772px;top:2110px;width:105px;height:28px;border-width:1.5px">Add to cart</div>

<!-- testimonials -->
<section class="testi" role="img" aria-label="Blurred warm red portrait backdrop">
  <p class="eyebrow">WHAT MY GUYS SAY ABOUT ME</p>
  <h2>Client Testimonials</h2>
  <p>Lorem ipsum dolor sit amet, consectetur adipiscing elit, sed do eiusmod tempor incididunt ut labore et dolore magna aliqua. Quis ipsum suspendisse ultrices gravida. Risus commodo viverra maecenas accumsan lacus vel facilisis.</p>
  <p class="client">Client Name</p>
  <div class="btn btn-light" style="left:544px;top:335px;width:96px;height:28px">Read more</div>
</section>

<!-- care -->
<p class="care-eyebrow">HEADING TEXT HERE</p>
<h2 class="care-title">How to take care of<br>your gym equipment</h2>
<p class="care-text">Curabitur neque ex, facilisis id venenatis in, tincidunt at augue. Etiam lobortis commodo tristique. Aliquam convallis pulvinar facilisis.</p>
<div class="btn btn-outline" style="left:193px;top:3082px;width:95px;height:28px;border-width:1.5px">Read more</div>
<div class="studio" style="left:599px;top:2823px;width:407px;height:381px">
  <div class="product-shot" role="img" aria-label="Yellow dumbbell and barbell plate set" style="left:50px;top:45px;width:307px;height:291px;background:linear-gradient(150deg,#ffc000 0%,#f8cf3a 45%,#2e2e30 100%)"></div>
</div>

<!-- trending -->
<p class="trend-eyebrow">POPULAR PRODUCTS</p>
<h2 class="trend-title">Trending now</h2>
<div class="tile" style="left:0"><div class="product-shot" role="img" aria-label="Ab roller wheel kit"></div></div>
<div class="tile" style="left:404px"><div class="product-shot" role="img" aria-label="Model using an ab crunch machine" style="background:linear-gradient(160deg,#3a3a3e 0%,#e0463a 45%,#1c1c1e 100%)"></div></div>
<div class="tile" style="left:807px"><div class="product-shot" role="img" aria-label="Adjustable workout bench"></div></div>
<div class="tile-meta" style="left:13px"><div class="stars"><span></span><span></span><span></span><span></span><span></span></div><h4>Product Name 9</h4><p class="p">$135.00</p></div>
<div class="tile-meta" style="left:417px"><div class="stars"><span></span><span></span><span></span><span></span><span></span></div><h4>Product Name 11</h4><p class="p">$185.00</p></div>
<div class="tile-meta" style="left:821px"><div class="stars"><span></span><span></span><span></span><span></span><span></span></div><h4>Product Name 10</h4><p class="p">$117.00</p></div>

<!-- footer -->
<footer class="footer">
  <div class="brand" style="left:190px;top:80px;font-size:17px;flex-direction:column;gap:6px;text-align:center;line-height:20px"><span class="dot" style="width:40px;height:40px"></span>Mabels<br>Trinket Nook</div>
  <div class="fcol" style="left:397px"><h5>ABOUT US</h5>Home<br>Women<br>Men<br>About Us<br>Contact</div>
  <div class="fcol" style="left:599px"><h5>USEFUL LINKS</h5>Privacy Policy<br>Refund Policy<br>Shipping Informations<br>Terms &amp; Conditions<br>FAQ's</div>
  <div class="fcol" style="left:802px"><h5>CONTACT</h5><span class="addr">48 Larkspur Row, Easton, PA 18042</span><br>hello@mabelsnook.com<br><span class="addr">555-318-2047</span></div>
  <p class="copy">Copyright 2023 MabelsTrinketNook.com &nbsp;|&nbsp; All rights reserved.</p>
  <div class="social"><span></span><span></span><span></span></div>
</footer>

</body>
</html>
```